Local Flower Farm Needs Business Card Design

I need business cards designed for a flower farm based in Eudora, Kansas.
Business Info:
We are a local cut flower farm located in Eudora, Kansas, founded by Darla Whitcombe. What started as a passion for agriculture and search for more joy in daily life has blossomed into a small business dedicated to providing the community with beautiful, fresh, and sustainable flowers. We specialize in local, seasonal blooms, ensuring that every petal reflects the care and dedication we pour into our craft. Our mission is to deliver the highest quality flowers directly to our customers through local farmers markets and to florists who share our commitment to sustainability. Join us in celebrating the beauty of nature, one bloom at a time!
Contact Details:
Darla Whitcombe
Owner
Phone 913-555-0148
Facebook: Rosalind Pike Gardens
Instagram: @RosalindPikeGardens
Website: RosalindPikeGardens.example
Target Market(s)
Wholesale to Florists and Direct to Consumer via Farmers Market
Industry/Entity Type
Florist, Farm
Contact Information for Business Card
Name, Contact Info, Logo
Look and feel
Each slider illustrates characteristics of the customer's brand and the style your logo design should communicate.

```html
<!DOCTYPE html>
<html lang="en">
<head>
<meta charset="utf-8">
<title>Rosalind Pike Gardens – Business Card</title>
<link rel="stylesheet" href="https://fonts.googleapis.com/css2?family=Playfair+Display:wght@400&family=Montserrat:wght@500;600&display=swap">
<style>
  :root {
    --forest: #22353a;
    --paper: #ffffff;
    --rim: #e6e6e6;
    --page: #ffffff;
    --shadow: rgba(0, 0, 0, 0.18);
  }
  html, body {
    margin: 0;
    width: 1200px;
    height: 1200px;
    overflow: hidden;
    background: var(--page);
  }
  .card {
    position: absolute;
    left: 287px;
    width: 634px;
    height: 362px;
    box-shadow: 0 12px 40px var(--shadow);
  }
  .card svg { display: block; width: 100%; height: 100%; }
  .card--front { top: 217px; }
  .card--back { top: 628px; }
  .brand-name {
    font-family: "Playfair Display", serif;
    font-weight: 400;
    fill: var(--paper);
  }
  .holder-name {
    font-family: "Playfair Display", serif;
    font-weight: 400;
    fill: var(--paper);
    font-size: 44px;
    letter-spacing: 0.5px;
  }
  .holder-role {
    font-family: "Montserrat", sans-serif;
    font-weight: 600;
    fill: var(--paper);
    font-size: 20px;
    letter-spacing: 1px;
  }
  .contact-line {
    font-family: "Montserrat", sans-serif;
    font-weight: 500;
    fill: var(--paper);
    font-size: 19px;
  }
  .icon-disc { fill: var(--paper); }
  .icon-glyph { fill: var(--forest); }
  .icon-line { fill: none; stroke: var(--forest); stroke-width: 2; }
</style>
</head>
<body>

<!-- Front of card -->
<div class="card card--front">
  <svg viewBox="0 0 1014 579" xmlns="http://www.w3.org/2000/svg">
    <rect class="card-field" width="1014" height="579" fill="var(--forest)"/>
    <polygon class="hex-panel" points="274,0 740,0 907,289 740,579 274,579 107,289" fill="var(--paper)"/>
    <g class="brand-mark">
      <circle cx="507" cy="289" r="222" fill="var(--forest)" stroke="var(--rim)" stroke-width="10"/>
      <text class="brand-name" x="507" y="276" text-anchor="middle" font-size="46">Rosalind Pike</text>
      <text class="brand-name" x="507" y="332" text-anchor="middle" font-size="46">Gardens</text>
    </g>
  </svg>
</div>

<!-- Back of card -->
<div class="card card--back">
  <svg viewBox="0 0 1014 579" xmlns="http://www.w3.org/2000/svg">
    <rect class="card-field" width="1014" height="579" fill="var(--paper)"/>
    <polygon class="info-panel" points="320,0 1014,0 1014,579 320,579 280,510 280,70" fill="var(--forest)"/>
    <circle class="badge-cutout" cx="294" cy="290" r="238" fill="var(--paper)"/>
    <g class="brand-mark">
      <circle cx="294" cy="290" r="222" fill="var(--forest)" stroke="var(--rim)" stroke-width="10"/>
      <text class="brand-name" x="294" y="277" text-anchor="middle" font-size="46">Rosalind Pike</text>
      <text class="brand-name" x="294" y="333" text-anchor="middle" font-size="46">Gardens</text>
    </g>

    <text class="holder-name" x="561" y="180" textLength="394" lengthAdjust="spacingAndGlyphs">DARLA WHITCOMBE</text>
    <text class="holder-role" x="562" y="212">OWNER</text>

    <g class="contact-list">
      <!-- phone -->
      <circle class="icon-disc" cx="580" cy="317" r="17"/>
      <path class="icon-glyph" d="M573 307c1.5-1 3-.5 3.5.5l2 4c.4 1-.2 1.8-1 2.3l-1 .6c.8 2 2.5 3.8 4.5 4.6l.6-1c.5-.8 1.3-1.4 2.3-1l4 2c1 .5 1.5 2 .5 3.5-1.5 2-4 2.6-6 1.6-4.5-2-8.3-5.8-10.3-10.3-1-2-.4-4.5 .9-6.8z"/>
      <text class="contact-line" x="613" y="324">913-555-0148</text>

      <!-- facebook page -->
      <circle class="icon-disc" cx="580" cy="361" r="17"/>
      <text class="contact-line" x="613" y="368">Rosalind Pike Gardens</text>

      <!-- instagram handle -->
      <circle class="icon-disc" cx="580" cy="406" r="17"/>
      <text class="contact-line" x="613" y="413">@RosalindPikeGardens</text>

      <!-- website -->
      <circle class="icon-disc" cx="580" cy="451" r="17"/>
      <circle class="icon-line" cx="580" cy="451" r="9"/>
      <ellipse class="icon-line" cx="580" cy="451" rx="4" ry="9"/>
      <line class="icon-line" x1="571" y1="451" x2="589" y2="451"/>
      <text class="contact-line" x="613" y="458">RosalindPikeGardens.example</text>
    </g>
  </svg>
</div>

</body>
</html>
```